New Health Business Needs Flyer for Africa

We are a new network marketing company about to launch in Africa. I need a flyer made purely for the business and earning opportunity that people can get with our company. This is a home based business that anyone can get involved with. Very low start up costs with high quality effective and innovative products. You can visit our blog to get more information on the benefits I would like to see on the flyer. http://tolvenpost.example. This flyer is to attract people who want to earn more money and build a long term business with financial security.
Updates

This needs to be about making more money. Luxury lifestyle, flash cars, big houses etc. I don't want anything about the product on this flyer

Reason: to give you all a bit more time on this I have extended the time period

Reason: to give you more time

Target Market(s)

anyone who wants to earn more money. Over 18 years old.

Industry/Entity Type

Marketing

Requirements
Must have
• This is a simple handout flyer A5 size. Can have front and back. Because we are opening in Africa, any faces or people should be black. It should have the logo which is uploaded to files also.

```html
<!DOCTYPE html>
<html lang="en">
<head>
<meta charset="utf-8">
<title>Soravine Global – Compensation Plan Flyer</title>
<link rel="stylesheet" href="https://fonts.googleapis.com/css2?family=PT+Sans+Narrow:wght@700&display=swap">
<style>
  :root {
    --brand-blue: #2a5aa8;
    --brand-green: #2ea646;
    --ink: #161616;
    --paper: #ffffff;
    --tick-grey: #a9a9a9;
    --page-shadow: 0 2px 6px rgba(0,0,0,0.35);
  }
  * { margin: 0; padding: 0; box-sizing: border-box; }
  html, body { width: 1200px; height: 1000px; overflow: hidden; background: var(--paper); }
  body { position: relative; font-family: "PT Sans Narrow", "Arial Narrow", sans-serif; font-weight: 700; }

  .flyer-page {
    position: absolute;
    overflow: hidden;
    background: var(--paper);
    box-shadow: var(--page-shadow);
  }
  .flyer-page .page-art { position: absolute; inset: 0; width: 100%; height: 100%; }

  .brand-name {
    position: absolute;
    color: var(--brand-green);
    font-weight: 700;
    line-height: 0.9;
    text-align: right;
  }
  .brand-name .brand-main,
  .brand-name .brand-sub { display: block; }

  /* ---------- Front ---------- */
  .front { left: 28px; top: 28px; width: 550px; height: 785px; }

  .front .brand-head { left: 60px; top: 70px; width: 450px; }
  .front .brand-head .brand-main { font-size: 118px; letter-spacing: 1px; }
  .front .brand-head .brand-sub { font-size: 44px; }

  .front .brand-foot { left: 320px; top: 706px; width: 205px; color: var(--paper); }
  .front .brand-foot .brand-main { font-size: 46px; }
  .front .brand-foot .brand-sub { font-size: 17px; }

  .benefit-list { list-style: none; }
  .benefit-item {
    position: absolute;
    display: flex;
    align-items: center;
    gap: 16px;
    font-size: 19px;
    color: var(--ink);
    letter-spacing: 0.2px;
    text-shadow: 0 0 4px rgba(255,255,255,0.9);
    white-space: nowrap;
  }
  .benefit-item svg { width: 24px; height: 20px; flex: none; }

  .plan-title {
    position: absolute;
    left: 160px; top: 555px;
    width: 440px;
    text-align: center;
    font-size: 23px;
    letter-spacing: 1px;
    color: var(--brand-blue);
    transform: rotate(-51deg);
    transform-origin: 50% 50%;
    white-space: nowrap;
  }

  /* ---------- Back ---------- */
  .back { left: 610px; top: 28px; width: 558px; height: 787px; }

  .bonus { position: absolute; }
  .bonus-title { font-size: 19px; letter-spacing: 0.3px; margin-bottom: 5px; }
  .bonus-text { font-size: 13.6px; line-height: 20.5px; }
  .bonus.on-green, .bonus.on-blue { color: var(--paper); }
  .bonus.on-white { color: var(--brand-blue); }
  .bonus.align-right { text-align: right; }
  .bonus.align-center { text-align: center; }

  .bonus.fast-start { left: 17px; top: 14px; }
  .bonus.extra-fast-start { right: 65px; top: 150px; }
  .bonus.new-car { left: 150px; top: 303px; width: 370px; }
  .bonus.luxury-holiday { left: 97px; top: 478px; }
  .bonus.loyalty { right: 23px; top: 645px; }

  .back .brand-foot { left: 36px; top: 696px; width: 140px; color: var(--paper); text-align: left; }
  .back .brand-foot .brand-main { font-size: 36px; }
  .back .brand-foot .brand-sub { font-size: 14px; }
</style>
</head>
<body>

<!-- Front of flyer -->
<section class="flyer-page front">
  <svg class="page-art" viewBox="0 0 550 785" preserveAspectRatio="none">
    <defs>
      <linearGradient id="coinsTone" x1="0" y1="0" x2="1" y2="1">
        <stop offset="0" stop-color="#ffffff"/>
        <stop offset="0.35" stop-color="#f1f3f5"/>
        <stop offset="0.6" stop-color="#cfd3d6"/>
        <stop offset="0.8" stop-color="#d8c79c"/>
        <stop offset="1" stop-color="#e8e9ea"/>
      </linearGradient>
    </defs>
    <g role="img" aria-label="Photo of stacked silver and gold coins on a soft blurred background">
      <rect x="0" y="0" width="550" height="785" fill="url(#coinsTone)"/>
    </g>
    <path class="band-blue" d="M0 0 L420 0 C270 90 110 320 20 785 L0 785 Z" fill="var(--brand-blue)"/>
    <path class="band-green" d="M550 120 C510 430 400 650 225 785 L550 785 Z" fill="var(--brand-green)"/>
  </svg>

  <div class="brand-name brand-head">
    <span class="brand-main">soravine</span>
    <span class="brand-sub">global</span>
  </div>

  <ul class="benefit-list">
    <li class="benefit-item" style="left:212px; top:266px;">
      <svg viewBox="0 0 24 20"><path d="M2 11 L9 17 L22 3" fill="none" stroke="var(--tick-grey)" stroke-width="4" stroke-linecap="round" stroke-linejoin="round"/></svg>
      LOW START-UP COSTS
    </li>
    <li class="benefit-item" style="left:190px; top:311px;">
      <svg viewBox="0 0 24 20"><path d="M2 11 L9 17 L22 3" fill="none" stroke="var(--tick-grey)" stroke-width="4" stroke-linecap="round" stroke-linejoin="round"/></svg>
      INNOVATIVE PRODUCTS
    </li>
    <li class="benefit-item" style="left:170px; top:357px;">
      <svg viewBox="0 0 24 20"><path d="M2 11 L9 17 L22 3" fill="none" stroke="var(--tick-grey)" stroke-width="4" stroke-linecap="round" stroke-linejoin="round"/></svg>
      FAST START BONUSES
    </li>
    <li class="benefit-item" style="left:155px; top:402px;">
      <svg viewBox="0 0 24 20"><path d="M2 11 L9 17 L22 3" fill="none" stroke="var(--tick-grey)" stroke-width="4" stroke-linecap="round" stroke-linejoin="round"/></svg>
      NEW CAR BONUSES
    </li>
    <li class="benefit-item" style="left:141px; top:449px;">
      <svg viewBox="0 0 24 20"><path d="M2 11 L9 17 L22 3" fill="none" stroke="var(--tick-grey)" stroke-width="4" stroke-linecap="round" stroke-linejoin="round"/></svg>
      LUXURY HOLIDAY BONUSES
    </li>
    <li class="benefit-item" style="left:131px; top:496px;">
      <svg viewBox="0 0 24 20"><path d="M2 11 L9 17 L22 3" fill="none" stroke="var(--tick-grey)" stroke-width="4" stroke-linecap="round" stroke-linejoin="round"/></svg>
      LOYALTY PAYMENTS
    </li>
  </ul>

  <p class="plan-title">SORAVINE GLOBAL COMPENSATION PLAN</p>

  <div class="brand-name brand-foot">
    <span class="brand-main">soravine</span>
    <span class="brand-sub">global</span>
  </div>
</section>

<!-- Back of flyer -->
<section class="flyer-page back">
  <svg class="page-art" viewBox="0 0 558 787" preserveAspectRatio="none">
    <defs>
      <linearGradient id="carTone" x1="0" y1="0" x2="0" y2="1">
        <stop offset="0" stop-color="#8d9195"/>
        <stop offset="0.6" stop-color="#c4c7ca"/>
        <stop offset="1" stop-color="#ffffff" stop-opacity="0"/>
      </linearGradient>
      <linearGradient id="beachTone" x1="0" y1="0" x2="0" y2="1">
        <stop offset="0" stop-color="#ffffff" stop-opacity="0"/>
        <stop offset="0.3" stop-color="#b9d6e6"/>
        <stop offset="0.6" stop-color="#2fb0c9"/>
        <stop offset="0.85" stop-color="#4f8a4a"/>
        <stop offset="1" stop-color="#d9cba4"/>
      </linearGradient>
    </defs>
    <g role="img" aria-label="Photo of a new silver saloon car">
      <rect x="340" y="0" width="218" height="140" fill="url(#carTone)"/>
    </g>
    <g role="img" aria-label="Photo of a tropical beach bay with turquoise water and palm trees">
      <rect x="0" y="590" width="310" height="197" fill="url(#beachTone)"/>
    </g>
    <path class="band-green" d="M0 0 L345 0 C250 110 110 300 0 490 Z" fill="var(--brand-green)"/>
    <path class="band-blue" d="M558 55 C525 360 430 610 278 787 L558 787 Z" fill="var(--brand-blue)"/>
  </svg>

  <article class="bonus fast-start on-green">
    <h2 class="bonus-title">FAST START BONUS!</h2>
    <p class="bonus-text">When you personally sponsor a new distributor,<br>you will earn a 10% commission on the CV<br>generated. There is NO limit to how many<br>people you can sponsor. For example,<br>when you sponsor a person who<br>purchases a Platinum Pack<br>you will earn $60 commission!</p>
  </article>

  <article class="bonus extra-fast-start on-white align-right">
    <h2 class="bonus-title">EXTRA FAST START BONUS!</h2>
    <p class="bonus-text">We want to reward you for working with and<br>helping those people who you personally refer.<br>Therefore to do this we will pay you Extra Fast Start<br>bonuses once you reach higher ranks within our company!</p>
  </article>

  <article class="bonus new-car on-white align-center">
    <h2 class="bonus-title">NEW CAR BONUS!</h2>
    <p class="bonus-text">Once you achieve the qualifications for this bonus,<br>we will buy you a new car, up to the value of $20,000!<br>It will be paid for completely. It can be a new car,<br>or any car of your choice. All you pay for is the insurance<br>and the gas to drive it!</p>
  </article>

  <article class="bonus luxury-holiday on-white">
    <h2 class="bonus-title">LUXURY HOLIDAY BONUS!</h2>
    <p class="bonus-text">When you have a monthly volume of CV100,00 in your<br>strong leg and a monthly volume of CV50,000 in your<br>lesser leg and you maintain that for 3 consecutive<br>months, you will qualify for a luxury vacation for<br>2 people. You can choose your destination or let<br>us send you to Hawaii or even Australia!</p>
  </article>

  <article class="bonus loyalty on-blue align-right">
    <h2 class="bonus-title">LOYALTY PAYMENTS!</h2>
    <p class="bonus-text">Once you achieve the Bronze rank<br>and maintain that for 3 consecutive<br>months, and have a minimum monthly<br>product order of CV50, you will quality to receive<br>a reward of $200 paid to your commission account!</p>
  </article>

  <div class="brand-name brand-foot">
    <span class="brand-main">soravine</span>
    <span class="brand-sub">global</span>
  </div>
</section>

</body>
</html>
```